Social responsible Renewable Energy company

We at voltaQ are an independent power producer company founded in 2021 that handles large scale deployment of Renewable Energy and carbon neutral Energy as a service model. We offer turnkey solutions using solar panel systems and this could be incorporated in our business cards. You can also find our logo in the documents provided. Another key issue is that the business cards will be printed on recicled paper, not sure if this is a limitation in deciding the design. The recycled sign should also be added on the business card and stating that the paper used was recycled. Our website is www.myvoltaq.example. It should also be very professional, not too dreamy but still needs to capture your imagination. We are really excited to get your ideas !

Target Market(s)

Renewable Energy market

Contact Information for Business Card

The business card will be printed on recycled paper. Name of the company is voltaQ. Website is www.myvoltaq.example

Requirements
Nice to have
• Our motto: Powered by renewable, driven by people.

```html
<!DOCTYPE html>
<html lang="en">
<head>
<meta charset="utf-8">
<title>voltaQ business card</title>
<link href="https://fonts.googleapis.com/css2?family=Poppins:wght@400;600&display=swap" rel="stylesheet">
<style>
  :root {
    --backdrop: #8f8580;
    --paper: #e3dac6;
    --ink-blue: #0f4c7f;
    --ink-grey: #7d776c;
    --watermark: #d2c9b6;
  }
  * { margin: 0; padding: 0; box-sizing: border-box; }
  html, body { width: 1200px; height: 864px; overflow: hidden; }
  body {
    background: var(--backdrop);
    font-family: "Poppins", sans-serif;
    display: flex; align-items: center; justify-content: center;
  }
  .card {
    position: relative;
    width: 980px; height: 560px;
    background: var(--paper);
    overflow: hidden;
  }
  .card__watermark {
    position: absolute; right: 70px; bottom: -60px;
    width: 420px; height: 420px; border-radius: 50%;
    background: var(--watermark);
  }
  .brand {
    position: absolute; left: 360px; top: 64px;
    display: flex; align-items: center; gap: 14px;
  }
  .brand__name {
    font-size: 64px; font-weight: 600; color: var(--ink-blue);
    letter-spacing: 1px; line-height: 1;
  }
  .brand__dot {
    width: 34px; height: 34px; border-radius: 50%; background: var(--ink-blue);
  }
  .person { position: absolute; left: 90px; top: 170px; }
  .person__name { font-size: 30px; font-weight: 600; color: var(--ink-blue); }
  .person__role { font-size: 22px; color: var(--ink-grey); }
  .contacts {
    position: absolute; left: 90px; top: 300px;
    list-style: none; font-size: 24px; color: var(--ink-grey);
  }
  .contacts li { display: flex; align-items: center; gap: 16px; line-height: 42px; }
  .contacts svg { width: 20px; height: 20px; flex: none; }
  .icon-fill { fill: var(--ink-blue); }
  .icon-line { fill: none; stroke: var(--ink-blue); stroke-width: 2.2; }
  .recycled-mark {
    position: absolute; right: 56px; top: 246px;
    width: 56px; height: 56px;
  }
  .recycled-mark__arrow { stroke: var(--ink-blue); stroke-width: 10; stroke-linecap: round; fill: none; }
  .recycled-mark__head { fill: var(--ink-blue); }
  .office {
    position: absolute; left: 600px; top: 410px;
    font-size: 22px; font-style: normal; color: var(--ink-grey); line-height: 32px;
  }
  .office__name { font-weight: 600; color: var(--ink-blue); }
</style>
</head>
<body>
  <article class="card">
    <div class="card__watermark" role="img" aria-label="Large faint brand decoration"></div>

    <header class="brand">
      <span class="brand__name">voltaQ</span>
      <span class="brand__dot"></span>
    </header>

    <section class="person">
      <p class="person__name">Daniel Reyes</p>
      <p class="person__role">Director</p>
    </section>

    <ul class="contacts">
      <li>
        <svg viewBox="0 0 24 24"><path class="icon-fill" d="M6.6 10.8a15 15 0 0 0 6.6 6.6l2.2-2.2a1 1 0 0 1 1-.25 11.4 11.4 0 0 0 3.6.57 1 1 0 0 1 1 1V20a1 1 0 0 1-1 1A17 17 0 0 1 3 4a1 1 0 0 1 1-1h3.5a1 1 0 0 1 1 1c0 1.25.2 2.45.57 3.57a1 1 0 0 1-.25 1z"/></svg>
        (555) 014.2290
      </li>
      <li>
        <svg viewBox="0 0 24 24"><rect class="icon-fill" x="2" y="5" width="20" height="14" rx="1.5"/><path d="M3 6l9 7 9-7" fill="none" stroke="#e3dac6" stroke-width="2"/></svg>
        info@myvoltaq.example
      </li>
      <li>
        <svg viewBox="0 0 24 24"><circle class="icon-line" cx="12" cy="12" r="9.5"/><ellipse class="icon-line" cx="12" cy="12" rx="4" ry="9.5"/><path class="icon-line" d="M2.5 12h19"/></svg>
        www.myvoltaq.example
      </li>
    </ul>

    <svg class="recycled-mark" viewBox="-50 -50 100 100" role="img" aria-label="Recycling sign: printed on recycled paper">
      <title>Printed on recycled paper</title>
      <g id="recycle-arrow">
        <path class="recycled-mark__arrow" d="M6 -30 L22 -2"/>
        <polygon class="recycled-mark__head" points="34,19 15,9 33,-2"/>
      </g>
      <use href="#recycle-arrow" transform="rotate(120)"/>
      <use href="#recycle-arrow" transform="rotate(240)"/>
    </svg>

    <address class="office">
      <p class="office__name">voltaQ</p>
      <p>4410 NW 18th St.</p>
      <p>Brightmoor, XL 40517</p>
    </address>
  </article>
</body>
</html>
```